Ridge 4 Ridge Turbine Rentals Pty Ltd

We are a hire company based on the Gold Coast in Australia, we Hire out Generators to construction sites, music festivals, parties, fetes etc. Anywhere where power is required we can provide it.

Ridge 4 Ridge Turbine Rentals pty Ltd also provides all leads, distribution boards, Qualified Electricians to perform all connections. we offer refuelling services and mechanical services. 24Hr on call service - to an actual english speaking operator.

Slogan ''Switched On, Wherever You Are"

Industry/Entity Type

Construction

Contact Information for Business Card

M: 0481265390
E: bookings@ridge4ridgeturbinerentals-example.com.au

```html
<!DOCTYPE html>
<html lang="en">
<head>
<meta charset="utf-8">
<title>Ridge 4 Ridge Turbine Rentals – Business Card</title>
<link href="https://fonts.googleapis.com/css2?family=Open+Sans:wght@400;600;700&display=swap" rel="stylesheet">
<style>
  :root {
    --page-bg: #d8d5d2;
    --card-black: #0d0d0e;
    --text-white: #f2f2f2;
    --text-grey: #d6d6d6;
    --accent-blue: #2f7fb5;
    --divider: #5a5a5a;
  }
  html, body {
    margin: 0;
    padding: 0;
    overflow: hidden;
  }
  body {
    width: 1200px;
    height: 814px;
    background: var(--page-bg);
    font-family: "Open Sans", Arial, sans-serif;
    position: relative;
  }
  .card {
    position: absolute;
    top: 252px;
    width: 540px;
    height: 310px;
    background: var(--card-black);
    box-shadow: 0 10px 28px rgba(0,0,0,0.28);
    color: var(--text-white);
  }
  .card--front { left: 40px; }
  .card--back { left: 620px; }

  .brand {
    display: flex;
    align-items: center;
    gap: 10px;
    font-weight: 700;
    color: var(--text-white);
    letter-spacing: 0.5px;
    white-space: nowrap;
  }
  .brand__mark {
    background: var(--text-white);
    flex: none;
  }

  /* front */
  .card--front .brand {
    position: absolute;
    left: 150px;
    top: 62px;
    font-size: 24px;
  }
  .card--front .brand__mark { width: 12px; height: 12px; }

  .person {
    position: absolute;
    right: 340px;
    top: 214px;
    text-align: right;
    white-space: nowrap;
  }
  .person__name {
    color: var(--accent-blue);
    font-size: 20px;
    font-weight: 400;
    line-height: 1.15;
  }
  .person__role {
    color: var(--text-white);
    font-size: 16px;
    line-height: 1.25;
  }
  .divider {
    position: absolute;
    left: 208px;
    top: 170px;
    width: 1px;
    height: 104px;
    background: var(--divider);
  }
  .contact {
    position: absolute;
    left: 220px;
    top: 174px;
    font-size: 11px;
    line-height: 1.55;
    color: var(--text-grey);
    white-space: nowrap;
  }
  .contact__address { margin: 0 0 4px; }
  .contact__line {
    display: flex;
    align-items: center;
    gap: 7px;
  }
  .contact__line svg { width: 11px; height: 11px; flex: none; }

  /* back */
  .card--back .brand {
    position: absolute;
    left: 0;
    right: 0;
    top: 98px;
    justify-content: center;
    font-size: 30px;
  }
  .card--back .brand__mark { width: 14px; height: 14px; }
  .slogan {
    position: absolute;
    left: 0;
    right: 0;
    top: 218px;
    margin: 0;
    text-align: center;
    font-size: 15px;
    font-weight: 600;
    color: var(--text-white);
  }
</style>
</head>
<body>
  <section class="card card--front" aria-label="Business card front">
    <div class="brand">
      <span class="brand__mark"></span>
      <span class="brand__name">Ridge 4 Ridge</span>
    </div>

    <div class="person">
      <div class="person__name">Daniel Harper</div>
      <div class="person__role">CEO/Founder</div>
    </div>

    <div class="divider"></div>

    <div class="contact">
      <p class="contact__address">42 Wattle Crescent<br>Burleigh Heads, QLD 4220</p>
      <div class="contact__line">
        <svg viewBox="0 0 12 12" aria-hidden="true">
          <rect x="3" y="0.5" width="6" height="11" rx="1.2" fill="none" stroke="var(--accent-blue)" stroke-width="1.2"/>
          <rect x="5" y="9.2" width="2" height="1" fill="var(--accent-blue)"/>
        </svg>
        <span>0481265390</span>
      </div>
      <div class="contact__line">
        <svg viewBox="0 0 12 12" aria-hidden="true">
          <rect x="0.5" y="2.5" width="11" height="7.5" fill="var(--accent-blue)"/>
          <path d="M0.8 2.8 L6 7 L11.2 2.8" fill="none" stroke="var(--card-black)" stroke-width="1"/>
        </svg>
        <span>bookings@ridge4ridgeturbinerentals-example.com.au</span>
      </div>
    </div>
  </section>

  <section class="card card--back" aria-label="Business card back">
    <div class="brand">
      <span class="brand__mark"></span>
      <span class="brand__name">Ridge 4 Ridge</span>
    </div>
    <p class="slogan">Switched On, Wherever You Are</p>
  </section>
</body>
</html>
```